Update the A4 Specials Page for Restaurant/Cafe

Provide a MINIMALIST attractive Specials page we can print weekly for our food and drink specials to give to our guests. Final design is to be provided in WORD Document so it can be easily edited by Manager. Should be black text and MINIMALIST to minimise ink usage as we print hundreds a week. We have UPLOADED the existing page as a template for you to update. Maybe logo can stay, see what you think. Or delete it and do something else. Keep it simple. Choose a good FONT. Could be a little playful with a cocktail ICON or something. Our existing menus can be seen at www.tallpinebistro.com.au and they are using font Alegreya. Please note we are unable to provide any feedback to designers, however we really do appreciate your time if you are submitting a design. Thank you for your participation.

```html
<!DOCTYPE html>
<html lang="en">
<head>
<meta charset="UTF-8">
<title>Tall Pine Bistro – Weekly Specials</title>
<link href="https://fonts.googleapis.com/css2?family=Fredoka:wght@600&family=Roboto+Condensed:wght@400;700&display=swap" rel="stylesheet">
<style>
  :root {
    --canvas-bg: #f2f2f4;
    --page-bg: #ffffff;
    --ink: #111111;
    --ink-soft: #333333;
    --rule: #d9d9d9;
    --band: #f1f1f1;
    --photo-warm: #efe3d6;
    --photo-cool: #ecebe7;
  }
  * { margin: 0; padding: 0; box-sizing: border-box; }
  html, body {
    width: 1200px; height: 1200px; overflow: hidden;
    background: var(--canvas-bg);
  }
  .specials-page {
    position: absolute; left: 216px; top: 58px;
    width: 766px; height: 1084px;
    background: var(--page-bg);
    overflow: hidden;
    font-family: "Roboto Condensed", Arial, sans-serif;
    color: var(--ink);
  }
  .photo-soup {
    position: absolute; left: 0; top: 0; width: 360px; height: 460px;
    background: radial-gradient(ellipse 70% 60% at 30% 40%, var(--photo-warm) 0%, rgba(239,227,214,0.5) 60%, rgba(255,255,255,0) 100%);
  }
  .photo-pastry {
    position: absolute; left: 0; top: 660px; width: 766px; height: 424px;
    background: radial-gradient(ellipse 60% 55% at 60% 50%, var(--photo-cool) 0%, rgba(236,235,231,0.5) 60%, rgba(255,255,255,0) 100%);
  }
  .brand-name {
    position: absolute; left: 74px; top: 66px; width: 208px;
    font-weight: 700; font-size: 30px; line-height: 34px;
    text-align: center; text-transform: uppercase; color: var(--ink);
  }
  .page-title {
    position: absolute; left: 446px; top: 168px;
    font-family: "Fredoka", Arial, sans-serif; font-weight: 600;
    font-size: 54px; line-height: 60px; color: var(--ink);
    text-transform: uppercase;
  }
  .menu-item { position: absolute; left: 94px; right: 92px; }
  .item-name { font-weight: 700; font-size: 22px; line-height: 26px; text-transform: uppercase; }
  .item-desc { font-size: 17px; line-height: 23px; color: var(--ink-soft); }
  .item-price { position: absolute; right: 0; top: 2px; font-weight: 700; font-size: 17px; }
  .section-heading {
    position: absolute; left: 94px; top: 636px;
    font-family: "Fredoka", Arial, sans-serif; font-weight: 600;
    font-size: 32px; line-height: 36px; color: var(--ink);
  }
  .beer-heading {
    position: absolute; left: 94px; top: 830px;
    font-weight: 700; font-size: 23px; line-height: 28px;
  }
  .beer-detail {
    position: absolute; left: 94px; top: 876px;
    font-size: 17px; line-height: 23px; color: var(--ink-soft);
  }
  .beer-detail .upper { text-transform: uppercase; }
  .beer-price { position: absolute; right: 92px; top: 876px; font-weight: 700; font-size: 17px; }
  .url-bar {
    position: absolute; left: 384px; top: 986px; width: 338px; height: 44px;
    background: var(--band); border: 1px solid var(--rule);
    display: flex; align-items: center; justify-content: flex-end; padding-right: 14px;
    font-weight: 700; font-size: 16px; color: var(--ink);
  }
</style>
</head>
<body>
  <main class="specials-page">
    <div class="photo-soup" role="img" aria-label="Photo of a bowl of minestrone soup with pasta and basil"></div>
    <div class="photo-pastry" role="img" aria-label="Photo of a layered filo pastry slice with walnuts and syrup on a plate"></div>

    <div class="brand-name">Tall Pine<br>Bistro</div>

    <h1 class="page-title">Weekly<br>Specials</h1>

    <section class="menu-item" style="top:376px">
      <div class="item-name">Chicken Filo</div>
      <div class="item-desc">Creamy Chicken with Pinenuts, wrapped in Filo Pastry.<br>Served with Side Salad &amp; Zulu Sauce</div>
      <div class="item-price">$24</div>
    </section>

    <section class="menu-item" style="top:488px">
      <div class="item-name">Minestrone Soup</div>
      <div class="item-desc">Served with Garlic Bread</div>
      <div class="item-price">$8</div>
    </section>

    <h2 class="section-heading">cocktail special</h2>

    <section class="menu-item" style="top:712px">
      <div class="item-name">Passionista</div>
      <div class="item-desc">Vodka, Passionfruit Pulp, Mango Puree<br>Top up with Ginger &amp; Lemon Kombucha</div>
      <div class="item-price">$17</div>
    </section>

    <h2 class="beer-heading">Craft Beer Special</h2>
    <div class="beer-detail"><span class="upper">Quiet Heron<br>Sun Burst</span><br>Tropical Pale Ale<br>4.8% Alc.</div>
    <div class="beer-price">$10</div>

    <div class="url-bar">www.tallpinebistro.com.au</div>
  </main>
</body>
</html>
```